Need Web Page Created

Our company is need to have 3 web pages created (home page, about, contact) using basic html (css is ok). Not looking to use flash or swf, but something that could be used on all browsers and platforms.

I've attached an example design as what we are looking for (as well as logo). The orangish color that is in the logo design should be used on web pages where shown.

Looking for a nice smooth transition between page to page and the page icons up at the top right hand corner should change color based on the page you are viewing (color change can be white or the orangish color from logo).

It Company

```html
<!DOCTYPE html>
<html lang="en">
<head>
<meta charset="utf-8">
<title>Nova Gear Lab</title>
<link rel="stylesheet" href="https://fonts.googleapis.com/css2?family=Open+Sans:ital,wght@0,300;0,400;0,600;0,700;1,400;1,600&display=swap">
<style>
:root{
  --orange:#f39120;
  --orange-deep:#e5801a;
  --white:#ffffff;
  --paper:#f1f1f1;
  --ink:#333333;
  --muted:#6b6b6b;
  --slate:#4d5859;
  --night:#101516;
  --footer:#050707;
  --line:#dddddd;
  --sans:'Open Sans', Arial, sans-serif;
}
*{box-sizing:border-box;margin:0;padding:0}
html,body{width:1200px;height:2452px;overflow:hidden}
body{font-family:var(--sans);color:var(--ink);background:var(--white);position:relative}

.site-header{position:absolute;left:0;top:0;width:1200px;height:112px;background:var(--white)}
.brand{position:absolute;left:101px;top:36px;display:flex;align-items:center;gap:10px;font-family:var(--sans);font-weight:400;font-size:30px;color:#555;letter-spacing:.5px}
.brand-dot{width:22px;height:22px;border-radius:50%;background:var(--orange)}
.nav-icons{position:absolute;right:100px;top:42px;display:flex;gap:28px}
.nav-icons svg{width:30px;height:28px;display:block}

.band{position:absolute;left:0;width:1200px;overflow:hidden}
.band-hero{top:112px;height:689px;background:var(--orange)}
.band-about{top:801px;height:801px;background:var(--paper)}
.band-contact{top:1602px;height:801px;background:var(--night)}

.gear-art{position:absolute;left:0;top:0;width:540px;height:100%}
.band-hero .gear-art{background:
  radial-gradient(circle at 170px 640px, var(--slate) 0 170px, transparent 171px),
  radial-gradient(circle at 40px 345px, var(--white) 0 330px, transparent 331px)}
.band-about .gear-art{background:
  radial-gradient(circle at 170px 755px, var(--slate) 0 170px, transparent 171px),
  radial-gradient(circle at 40px 460px, #fcfcfc 0 330px, transparent 331px)}
.band-contact .gear-art{background:
  radial-gradient(circle at 170px 755px, var(--slate) 0 170px, transparent 171px),
  radial-gradient(circle at 40px 480px, #fcfcfc 0 330px, transparent 331px)}

.hero-title{position:absolute;right:105px;top:20px;font-weight:300;font-size:86px;color:#fbe3c6;letter-spacing:1px;line-height:1.1}
.hero-tagline{position:absolute;right:105px;top:270px;font-weight:700;font-size:54px;line-height:64px;color:var(--white);text-align:right}
.quote{position:absolute;right:105px;text-align:right;font-style:italic;font-size:18px;line-height:25px}
.quote-author{display:block;font-style:normal;font-weight:600;margin-top:14px;font-size:17px}
.band-hero .quote{top:566px;color:#5a3300}
.band-hero .quote-author{color:#6b3f07}

.section-title{position:absolute;right:105px;top:65px;font-weight:300;font-size:86px;color:#707070;line-height:1.1}
.card{position:absolute;top:237px;width:322px;height:371px;background:var(--white);border:1px solid var(--line);border-radius:3px;padding:14px 18px}
.card-mission{left:433px}
.card-experience{left:768px}
.card h2{font-weight:400;font-size:30px;color:var(--orange);margin-bottom:12px}
.card p{font-size:13.5px;line-height:23px;color:var(--muted);margin-bottom:12px}
.card strong{font-weight:400;color:#222}
.band-about .quote{top:680px;color:#222}
.band-about .quote-author{color:var(--orange-deep)}

.contact-intro{position:absolute;right:105px;top:53px;width:330px;text-align:right;font-size:18.5px;line-height:25px;color:#e6e6e6}
.contact-card{position:absolute;left:768px;top:142px;width:322px;height:550px;background:var(--white);border-radius:3px;overflow:hidden}
.card-brand{display:flex;justify-content:center;align-items:center;gap:10px;padding-top:48px;font-weight:400;font-size:30px;color:#555}
.address{position:absolute;left:16px;top:115px;width:178px;text-align:right;font-size:13px;line-height:23px;color:#222}
.map{position:absolute;left:201px;top:118px;width:107px;height:108px;background:linear-gradient(135deg,#e9e6df,#d8d5ce);border:1px solid #ccc}
.contact-form{position:absolute;left:0;top:254px;width:322px;height:296px;background:#eeeeee;padding:20px 25px}
.field{display:block;width:271px;height:42px;background:var(--white);border:1px solid #d8d8d8;border-radius:2px;margin-bottom:11px;padding:10px 12px;font-family:var(--sans);font-size:13px;color:#999}
.field-message{height:93px}
.actions{position:absolute;left:906px;top:702px;display:flex;gap:8px}
.btn{height:40px;border:0;font-family:var(--sans);font-weight:600;font-size:17px;color:var(--white);text-transform:uppercase}
.btn-clear{width:83px;background:linear-gradient(#6d6d6d,#4a4a4a)}
.btn-submit{width:93px;background:var(--orange)}

.site-footer{position:absolute;left:0;top:2403px;width:1200px;height:49px;background:var(--footer)}
.copyright{position:absolute;left:101px;top:17px;font-size:12px;color:#888}
.social{position:absolute;right:100px;top:15px;display:flex;gap:16px}
.social span{width:18px;height:18px;border-radius:50%;background:#777}
</style>
</head>
<body>

<header class="site-header">
  <div class="brand"><span>NOVA GEAR LAB</span><span class="brand-dot"></span></div>
  <nav class="nav-icons" aria-label="Pages">
    <svg viewBox="0 0 30 28" aria-label="Home"><path d="M15 2 L28 14 H24 V26 H18 V18 H12 V26 H6 V14 H2 Z" fill="#f39120"/></svg>
    <svg viewBox="0 0 30 28" aria-label="About"><circle cx="15" cy="14" r="13" fill="#c9c9c9"/><rect x="13.3" y="12" width="3.4" height="10" fill="#fff"/><circle cx="15" cy="8" r="2" fill="#fff"/></svg>
    <svg viewBox="0 0 30 28" aria-label="Contact"><rect x="1" y="5" width="28" height="19" fill="#c9c9c9"/><path d="M1 5 L15 16 L29 5" fill="none" stroke="#fff" stroke-width="2"/></svg>
  </nav>
</header>

<section class="band band-hero">
  <div class="gear-art" role="img" aria-label="Large white gear with a smaller slate gear below"></div>
  <h1 class="hero-title">NOVA GEAR LAB</h1>
  <p class="hero-tagline">Today’s Idea for<br>Tomorrow’s Technology</p>
  <blockquote class="quote">" One's mind, once stretched by a new idea, never<br>regains its original dimensions."<span class="quote-author">- HAROLD WEXLEY BRANDT</span></blockquote>
</section>

<section class="band band-about">
  <div class="gear-art" role="img" aria-label="Large white gear with a smaller slate gear below"></div>
  <h2 class="section-title">What if......</h2>
  <article class="card card-mission">
    <h2>Mission</h2>
    <p><strong>At Nova Gear Lab</strong> , our mission is to provide the highest quality solutions to our clients that fits all of their needs. We listen to the client's needs and find the best solutions with our associates based on skills and background regardless if associate is located remotely or onsite.</p>
    <p><strong>Nova Gear Lab</strong> also believes in treating everyone with respect, integrity and honesty and to exceed client expectations.</p>
  </article>
  <article class="card card-experience">
    <h2>Experience</h2>
    <p>Nova Gear Lab is an outside-the-box thinker for tomorrow's solutions.</p>
    <p>We are a technology company that holds several patents for emerging technology with our management team having over 50 combined years on providing solutions .</p>
    <p>We are also a “think tank”, where no question or idea is ever far-fetch and the “what-if” question is a daily occurrence.</p>
    <p>We are providing solutions on today's idea for tomorrow's technology.</p>
  </article>
  <blockquote class="quote">" No idea is so outlandish that it should not be<br>considered "<span class="quote-author">- EDMUND CARROW HALE</span></blockquote>
</section>

<section class="band band-contact">
  <div class="gear-art" role="img" aria-label="Large white gear with a smaller slate gear below"></div>
  <p class="contact-intro">If you have questions pertaining to our patents or anything else, please feel free to contact us.</p>
  <div class="contact-card">
    <div class="card-brand"><span>NOVA GEAR LAB</span><span class="brand-dot"></span></div>
    <address class="address" style="font-style:normal">Nova Gear Lab<br>480 Meridian Avenue<br>2nd Floor<br>Harbor City, NY 10990<br>Phone (USA): 555-014-2290</address>
    <div class="map" role="img" aria-label="Street map showing the office location"></div>
    <form class="contact-form">
      <input class="field" type="text" placeholder="Name">
      <input class="field" type="email" placeholder="E-mail">
      <input class="field" type="tel" placeholder="Phone">
      <textarea class="field field-message" placeholder="Message"></textarea>
    </form>
  </div>
  <div class="actions">
    <button class="btn btn-clear" type="button">Clear</button>
    <button class="btn btn-submit" type="button">Submit</button>
  </div>
</section>

<footer class="site-footer">
  <p class="copyright">Copyright © 2014 NGL. All rights reserved</p>
  <div class="social" aria-label="Social links"><span></span><span></span><span></span></div>
</footer>

</body>
</html>
```